Biz Cards for Velmora Associates

Velmora Associates is seeking a single-sided business card that is more visually-appealing than our current design (see attached).

Notes:
- Our colors are blue & teal.
- Our tag line must be large enough to be easily read
- We don't necessarily need our address included (that's just the biz office)
- We'd like to add our email address: Velmora417@quillbox.net

Thanks!

Industry/Entity Type

Business

Contact Information for Business Card

Standard size
PSD file required w/ text on its own layer

Colors
86cfc6
3277b5

```html
<!DOCTYPE html>
<html lang="en">
<head>
<meta charset="utf-8">
<title>Velmora Associates – Business Card</title>
<link rel="stylesheet" href="https://fonts.googleapis.com/css2?family=Martel:wght@300;400&family=Jost:wght@300&family=Open+Sans:ital,wght@1,500&display=swap">
<style>
  :root {
    --page-bg: #ffffff;
    --card-bg: #fefefe;
    --card-border: #8a8a8a;
    --ink: #1f1f1f;
    --brand-blue: #3277b5;
    --brand-teal: #86cfc6;
    --tagline-blue: #1f6fc0;
  }
  * { margin: 0; padding: 0; box-sizing: border-box; }
  html, body {
    width: 1200px;
    height: 1200px;
    overflow: hidden;
    background: var(--page-bg);
  }
  .canvas {
    position: relative;
    width: 1200px;
    height: 1200px;
  }
  .card {
    position: absolute;
    left: 69px;
    top: 290px;
    width: 1062px;
    height: 621px;
    background: var(--card-bg);
    border: 1px solid var(--card-border);
  }
  .brand {
    position: absolute;
    left: 70px;
    top: 16px;
    width: 330px;
    text-align: center;
  }
  .brand-mark {
    display: block;
    margin: 0 auto 6px;
  }
  .brand-name {
    font-family: "Martel", serif;
    font-weight: 400;
    color: var(--ink);
    line-height: 1;
  }
  .brand-name .line-main {
    display: block;
    font-size: 52px;
    letter-spacing: 1px;
  }
  .brand-name .line-sub {
    display: block;
    font-size: 19px;
    letter-spacing: 9px;
    margin-top: 0;
  }
  .person {
    position: absolute;
    left: 403px;
    top: 0;
    right: 0;
    bottom: 0;
  }
  .person > * {
    position: absolute;
    left: 0;
    white-space: nowrap;
    line-height: 1;
    font-weight: normal;
  }
  .person-name {
    top: 247px;
    font-family: "Jost", sans-serif;
    font-weight: 300;
    font-size: 54px;
    color: var(--brand-blue);
    letter-spacing: 1.5px;
  }
  .person-title {
    top: 316px;
    font-family: "Martel", serif;
    font-weight: 300;
    font-size: 30px;
    color: var(--brand-teal);
    letter-spacing: 1.5px;
  }
  .contact {
    font-family: "Martel", serif;
    font-weight: 300;
    font-size: 27px;
    color: var(--ink);
    letter-spacing: 2px;
  }
  .contact-phone { top: 360px; }
  .contact-fax   { top: 402px; }
  .contact-email { top: 444px; }
  .contact-web   { top: 486px; }
  .tagline {
    top: 561px;
    font-family: "Open Sans", sans-serif;
    font-style: italic;
    font-weight: 500;
    font-size: 18.5px;
    color: var(--tagline-blue);
    letter-spacing: -0.3px;
  }
</style>
</head>
<body>
<main class="canvas">
  <section class="card">
    <div class="brand">
      <svg class="brand-mark" width="156" height="156" viewBox="0 0 156 156" aria-hidden="true">
        <circle cx="78" cy="78" r="76" fill="none" stroke="var(--ink)" stroke-width="2"/>
      </svg>
      <div class="brand-name">
        <span class="line-main">VELMORA</span>
        <span class="line-sub">ASSOCIATES Ltd</span>
      </div>
    </div>

    <div class="person">
      <h1 class="person-name">DANA WHITCOMBE, RN</h1>
      <p class="person-title">Mental Health Therapist</p>
      <p class="contact contact-phone">[p] (855) 555-0142</p>
      <p class="contact contact-fax">[f]&nbsp; (330) 555-0187</p>
      <p class="contact contact-email">Velmora417@quillbox.net</p>
      <p class="contact contact-web">VelmoraAssoc.net</p>
      <p class="tagline">Caring Minds. Gentle Hands. Brighter Days Ahead.</p>
    </div>
  </section>
</main>
</body>
</html>
```